Design Letterhead and Business Card for a travel company

Please refer to the attached document for the details to be included in the letterhead and business cards. Logo and contact details enclosed therein. Client is looking for a professional image.

Please include as many contact details as possible in your entries.

```html
<!DOCTYPE html>
<html lang="en">
<head>
<meta charset="utf-8">
<title>Skyvane Business Card</title>
<link rel="stylesheet" href="https://fonts.googleapis.com/css2?family=Lato:wght@400;700&display=swap">
<style>
  :root {
    --backdrop: #e9eaec;
    --card: #ffffff;
    --sky-blue: #29a3e0;
    --ink-grey: #5e6166;
    --text-dark: #333539;
    --brand-purple: #4b2a7b;
  }
  * { margin: 0; padding: 0; box-sizing: border-box; }
  html, body {
    width: 1200px;
    height: 749px;
    overflow: hidden;
    background: var(--backdrop);
    font-family: "Lato", Arial, sans-serif;
  }
  .canvas {
    position: relative;
    width: 1200px;
    height: 749px;
  }
  .card {
    position: absolute;
    top: 220px;
    width: 540px;
    height: 309px;
    background: var(--card);
    box-shadow: 0 6px 18px rgba(0, 0, 0, 0.12);
    overflow: hidden;
  }
  .card--front { left: 40px; }
  .card--back { left: 620px; }
  .card__band {
    position: absolute;
    left: 0;
    right: 0;
    bottom: 0;
    height: 13px;
    background: var(--sky-blue);
  }
  .brand {
    position: absolute;
    display: flex;
    align-items: center;
    gap: 10px;
    color: var(--sky-blue);
    font-weight: 700;
    font-size: 40px;
    letter-spacing: 1px;
  }
  .brand__dot {
    width: 22px;
    height: 22px;
    border-radius: 50%;
    background: var(--brand-purple);
  }
  .card--front .brand { left: 140px; top: 70px; }
  .card--back .brand { left: 50%; top: 100px; transform: translateX(-50%); }
  .person {
    position: absolute;
    right: 30px;
    top: 128px;
    text-align: right;
  }
  .person__name {
    font-size: 20px;
    color: var(--ink-grey);
    font-weight: 400;
  }
  .person__surname { color: var(--sky-blue); font-weight: 700; }
  .person__role {
    font-size: 11px;
    color: var(--text-dark);
    letter-spacing: 0.5px;
    margin-top: 2px;
  }
  .card__tab {
    position: absolute;
    right: 0;
    top: 130px;
    width: 12px;
    height: 38px;
    background: var(--sky-blue);
  }
  .contacts {
    position: absolute;
    left: 34px;
    bottom: 44px;
    list-style: none;
    font-size: 14px;
    color: var(--text-dark);
  }
  .contacts li {
    display: flex;
    align-items: center;
    gap: 10px;
    margin-top: 9px;
  }
  .contacts svg { width: 15px; height: 15px; flex: none; }
  .web-line {
    position: absolute;
    left: 0;
    right: 0;
    top: 204px;
    display: flex;
    justify-content: center;
    align-items: center;
    gap: 9px;
    font-size: 15px;
    color: var(--text-dark);
  }
  .web-line svg { width: 16px; height: 16px; }
</style>
</head>
<body>
<main class="canvas">
  <section class="card card--front">
    <div class="brand"><span class="brand__dot"></span>SKYVANE</div>
    <div class="person">
      <p class="person__name">Tamsin <span class="person__surname">Moyo</span></p>
      <p class="person__role">DIRECTOR / OWNER</p>
    </div>
    <div class="card__tab"></div>
    <ul class="contacts">
      <li>
        <svg viewBox="0 0 24 24" aria-hidden="true"><path fill="#333539" d="M6.6 10.8a15 15 0 0 0 6.6 6.6l2.2-2.2a1 1 0 0 1 1-.25 11.4 11.4 0 0 0 3.6.57 1 1 0 0 1 1 1V20a1 1 0 0 1-1 1A17 17 0 0 1 3 4a1 1 0 0 1 1-1h3.5a1 1 0 0 1 1 1c0 1.25.2 2.45.57 3.57a1 1 0 0 1-.25 1z"/></svg>
        071 555 03862
      </li>
      <li>
        <svg viewBox="0 0 24 24" aria-hidden="true"><rect x="2.5" y="5" width="19" height="14" fill="none" stroke="#333539" stroke-width="2"/><path d="M3 6l9 7 9-7" fill="none" stroke="#333539" stroke-width="2"/></svg>
        info@skyvane.co.za
      </li>
      <li>
        <svg viewBox="0 0 24 24" aria-hidden="true"><rect x="2.5" y="4" width="19" height="12" fill="none" stroke="#333539" stroke-width="2"/><path d="M8 20h8M12 16v4" stroke="#333539" stroke-width="2"/></svg>
        www.skyvane.co.za
      </li>
    </ul>
    <div class="card__band"></div>
  </section>

  <section class="card card--back">
    <div class="brand"><span class="brand__dot"></span>SKYVANE</div>
    <p class="web-line">
      <svg viewBox="0 0 24 24" aria-hidden="true"><circle cx="12" cy="12" r="10" fill="none" stroke="#333539" stroke-width="2"/><path d="M10 8l5 4-5 4z" fill="#333539"/></svg>
      www.skyvane.co.za
    </p>
    <div class="card__band"></div>
  </section>
</main>
</body>
</html>
```